Store Front Window Design

We have a beautiful corner store front dental practice with no window signage. Crazy I know...that's why we need your help.

The final design will be done in all vinyl unless unless you suggest a different medium (meaning we are open to some design idea like using frosted glass, etc...).

The windows provide a lot of natural light so the design needs to keep a lot of natural light coming into the office. Keep in mind vinyl is not opaque so keep the signage aesthetically pleasing and a minimalist design to allow as much natural light in as possible. The design should follow the aesthetic from our logo. or tie into at least. We want a cohesive brand aesthetic.

I submitted some general layout ideas. There is a blue banner with advertising words which we want to be used in the final version. Even though the lettering is black, in reality the letters will be a white vinyl on the outside of the window. When you submit your work, be sure to add any special instructions (aka tell me the vision for the letters is white not black, maybe gold leaf, or forested glass...stuff like that). AND YOU DO NOT HAVE TO FOLLOW MY PATTERN! YOU ARE ARTISTS AND WE ARE LOOKING FOR AN ARTISTIC EYE CATCHING PRESENTATION OF THIS INFORMATION. MAKE IT FLASHY AND ADD SOME AESTHETIC FROM THE TOOTH LOGO.

The store front is 6 windows roughly 60'' x 36'' The smaller windows below are 27'' x 36''. Around the corner there are 3 windows. they are 60'' x 27'' lower windows are 27" x 27". We would like to keep the bottom windows clear and keep the signage on the top windows, however, we are flexible.

The front 6 windows need to have this information worked into the design.

Practice name: Vesk and Ormond Dental & Orthodontics.
Phone numbers: Marisol Vesk DDS: 415.772.0183
Tobias Ormond DDS:415.509.2371

Expertise: Dr. Vesk General Dentistry & Orthodontics
Dr. Ormond Oral Surgery & Sedation

Address: 1937 Birchwood Ave

A banner across the bottom of the top windows with some key advertisement words: "Clarivet" "Braces" "Implants" "Whiting" "Call today" "Free Consultation" "Oral Surgery" "Sedation". We like the two color idea. Its up to you to decide on the color combo. I used a Dark and light blue, but maybe a Blue and grey would nice to tire in the logo colors?

I have made some mock ideas to get the ball rolling but you do not have to stick to these designs at all, just as long as all the required information is there. Be creative with the layouts, fonts, color scheme, (just remember these are going on windows not necessarily a white background), and graphics/artistic flare (refer to logo for layout inspiration and use the logo as an actual graphic). We are running a miltimillion dollar dental practice so we want these windows to be eye catching to pull in patients and look like a million dollar design. Also all 6 windows dont need ot be used. I am really looking for creative design marketing.

The corner 3 windows need the following information: name, expertise, phone number, banner.

Dr. Vesk, General Dentistry & Orthodontics, 415.772.0183
Dr. Ormond, Oral Surgery & Sedation, 415.509.2371

There is also a front door that needs to be designed. The door is 60'' x 36'' (standard door size) We want simple white vinyl on the outside of the door. We need you to organize the information on the door, pick a easy to read font, maybe use the logo and use some of the front window signage aesthetic? Its up to you...but we we were initially thinking of just making the litters white and keep it simple but again you are the designers.

Practice name: Vesk and Ormond General Dentistry & Orthodontics

Address: 1937 Birchwood Ave

Phone numbers: Dr. Vesk 415.772.0183
Dr. Ormond 415.509.2371

Hours of operation: Mon: call for an appointment
Tues-Thurs: 9am-5pm
Sat: call for an appointment
Sun: Closed

A line saying we speak Spanish: Se Habla Espanol

*****************************************************************************************************
here are some design that we liked and some rough sketches I made to start the ball rolling. Keep in mind that there are 9 windows for the front because its a corner office, but not all of them have to have stuff on it. We want simple, streamline, classy high commanding price point aesthetic. I am hiring you for your artistic minds.

Target Market(s)

anyone who has dental needs

Industry/Entity Type

Dental

Font styles to use
Serif
Sans Serif

Colors

Designer to choose colors to be used in the design.

Requirements
Must have
• 1. The required information (see project description)
• 2. Logo
• 3. Advertisement banner running along the bottom of all 9 windows (6 in front and 3 on the side)
• NOTE: Look at pictures of the store to get a sense of the customers point of view and also as a reference to how your design will be broken up across several windows or maybe you design something special for every window. But we want the banner to run along all the windows to lead customs to the door on the side. Finally the letters will be done in white vinyl unless state otherwise, remember the window needs to let in natural light so the entire window can not be covered in vinyl.
Nice to have
• artistic flare yet simple and sleep and expensive looking aesthetic. work logo into the design.
Should not have
• The goal is to catch someone eye and give them important information about the practice.
• It should not just be words.
• It should not have to many words
• It must be readable font for cards driving by.

```html
<!DOCTYPE html>
<html lang="en">
<head>
<meta charset="utf-8">
<title>Vesk and Ormond Dental &amp; Orthodontics – Front Door</title>
<link href="https://fonts.googleapis.com/css2?family=Bebas+Neue&family=Oswald:wght@300&family=Mulish:wght@400;500&family=Great+Vibes&display=swap" rel="stylesheet">
<style>
  :root{
    --backdrop:#e3e3e3;
    --brand-blue:#1a80d2;
    --title-blue:#0f6ec0;
    --band-grey:#a5a6a8;
    --tab-grey:#8b8c8e;
    --name-grey:#7b7c7e;
    --text-grey:#555;
    --white:#ffffff;
  }
  *{margin:0;padding:0;box-sizing:border-box}
  html,body{width:1200px;height:960px;overflow:hidden;background:var(--backdrop)}
  .canvas{position:relative;width:1200px;height:960px}
  .door-sign{
    position:absolute;left:331px;top:32px;width:560px;height:932px;
    transform:scale(0.96);transform-origin:top left;
    overflow:hidden;background:var(--white);
    box-shadow:0 4px 10px rgba(0,0,0,.18);
  }
  .sign-shapes{position:absolute;inset:0;width:560px;height:932px}
  .brand-mark{
    position:absolute;left:50%;top:80px;transform:translateX(-50%);
    width:74px;height:74px;border-radius:50%;background:var(--band-grey);
  }
  .brand-name{
    position:absolute;left:0;width:560px;top:196px;text-align:center;
    font-family:"Mulish",sans-serif;font-weight:500;color:var(--name-grey);
    font-size:26px;line-height:32px;
  }
  .practice-title{
    position:absolute;left:0;width:560px;top:322px;text-align:center;
    font-family:"Bebas Neue",sans-serif;font-size:90px;line-height:90px;color:var(--title-blue);
  }
  .practice-banner{
    position:absolute;left:0;top:412px;width:560px;height:45px;background:var(--brand-blue);
    color:var(--white);text-align:center;font-family:"Mulish",sans-serif;font-weight:500;
    font-size:33px;line-height:45px;
  }
  .practice-address{
    position:absolute;left:0;width:560px;top:468px;text-align:center;
    font-family:"Mulish",sans-serif;font-size:17px;line-height:24px;color:var(--text-grey);
  }
  .doctor{position:absolute;top:516px;width:280px;text-align:center}
  .doctor--vesk{left:17px}
  .doctor--ormond{left:291px}
  .doctor-name{font-family:"Bebas Neue",sans-serif;font-size:31px;line-height:34px;color:var(--title-blue)}
  .doctor-field{font-family:"Mulish",sans-serif;font-size:13px;color:var(--text-grey);margin-top:3px}
  .doctor-phone{font-family:"Oswald",sans-serif;font-weight:300;font-size:29px;color:var(--title-blue);margin-top:2px}
  .hours-tab{
    position:absolute;left:0;top:676px;width:262px;height:39px;background:var(--tab-grey);
    color:var(--white);font-family:"Bebas Neue",sans-serif;font-size:35px;line-height:41px;padding-left:18px;
  }
  .hours-list{position:absolute;left:18px;top:722px;list-style:none;
    font-family:"Mulish",sans-serif;font-size:17px;color:var(--brand-blue);line-height:28px}
  .spanish-line{
    position:absolute;right:14px;top:852px;font-family:"Great Vibes",cursive;
    font-size:42px;color:var(--white);
  }
</style>
</head>
<body>
<main class="canvas">
  <section class="door-sign">
    <svg class="sign-shapes" viewBox="0 0 560 932" aria-hidden="true">
      <rect class="corner-grey" x="0" y="0" width="560" height="330" fill="var(--band-grey)"/>
      <path class="top-sweep" d="M300 0 H560 V70 L120 150 C190 70 250 25 300 0 Z" fill="var(--brand-blue)"/>
      <path class="bottom-sweep" d="M560 470 V932 H0 V830 Z" fill="var(--brand-blue)"/>
      <path class="bottom-band" d="M0 845 C150 846 270 832 380 790 C270 862 130 898 0 906 Z" fill="var(--band-grey)"/>
      <path class="sign-body" d="M0 300 C40 140 230 35 560 35 V520 C520 700 380 840 0 850 Z" fill="var(--white)"/>
    </svg>

    <div class="brand-mark"></div>
    <p class="brand-name">Vesk and Ormond<br>Dental &amp; Orthodontics</p>

    <h1 class="practice-title">VESK &amp; ORMOND</h1>
    <div class="practice-banner">DENTAL &amp; ORTHODONTICS</div>
    <p class="practice-address">1937 Birchwood Ave</p>

    <div class="doctor doctor--vesk">
      <p class="doctor-name">DR. VESK</p>
      <p class="doctor-field">General Dentistry &amp; Orthodontics</p>
      <p class="doctor-phone">415.772.0183</p>
    </div>
    <div class="doctor doctor--ormond">
      <p class="doctor-name">DR. ORMOND</p>
      <p class="doctor-field">Oral Surgery &amp; Sedation</p>
      <p class="doctor-phone">415.509.2371</p>
    </div>

    <h2 class="hours-tab">HOURS OF OPERATION</h2>
    <ul class="hours-list">
      <li>Mon : Call for an appointment</li>
      <li>Tues - Thurs : 9am-5pm</li>
      <li>Sat : Call for an appointment</li>
      <li>Sun : Closed</li>
    </ul>

    <p class="spanish-line">Se Habla Espanol</p>
  </section>
</main>
</body>
</html>
```